Wine Label front and back- Need to have an eye catching, classy wine label for restaurant placement.

label design for a wine label. eye catching for shelf placement. looking for simple and elegant label. Name of the vineyard will be the label recognition. Need back label to match with coloring and basic regulated info required by gov't (producer, address, and statement) Back label will be addressed after selected front label to match.
Will add $100 extra for the back label to match.

Target Market(s)

40-65 year old foodies

Colors
0355a3
eaf1f7

Requirements
Must have
• FERNHOLLOW (label name)
Estate,
Red Wine Blend NV,

```html
<!DOCTYPE html>
<html lang="en">
<head>
<meta charset="utf-8">
<title>Fernhollow Estate – Front Label</title>
<link href="https://fonts.googleapis.com/css2?family=Playfair+Display:ital,wght@0,400;0,700;1,400&family=Montserrat:wght@400&display=swap" rel="stylesheet">
<style>
  :root {
    --brand-blue: #0355a3;
    --pale-blue: #eaf1f7;
    --label-white: #f7f7f7;
    --ink: #1a1a1a;
    --gold: #c9a54a;
    --map-tone-a: #f8f6ef;
    --map-tone-b: #f3efe2;
  }
  * { box-sizing: border-box; margin: 0; padding: 0; }
  html, body {
    width: 1200px;
    height: 1200px;
    overflow: hidden;
  }
  body {
    background: var(--pale-blue);
    position: relative;
  }
  .label {
    position: absolute;
    left: 50px;
    top: 98px;
    width: 1100px;
    height: 1004px;
    background: var(--label-white);
    overflow: hidden;
  }
  .label__band {
    position: absolute;
    left: 0;
    width: 100%;
    height: 29px;
    background: var(--brand-blue);
  }
  .label__band--top { top: 0; }
  .label__band--bottom { bottom: 0; }
  .label__map {
    position: absolute;
    left: 0;
    top: 29px;
    width: 100%;
    height: calc(100% - 58px);
    background: radial-gradient(ellipse at 50% 55%, var(--map-tone-b) 0%, var(--map-tone-a) 55%, var(--label-white) 100%);
  }
  .label__content {
    position: absolute;
    inset: 0;
    text-align: center;
  }
  .brand-mark {
    position: absolute;
    left: 0;
    right: 0;
    top: 206px;
    display: flex;
    justify-content: center;
    align-items: center;
    gap: 12px;
    font-family: "Playfair Display", serif;
    font-weight: 400;
    font-size: 26px;
    letter-spacing: 0.2em;
    color: var(--gold);
  }
  .brand-mark__dot {
    width: 12px;
    height: 12px;
    border-radius: 50%;
    background: var(--gold);
  }
  .wine-name {
    position: absolute;
    left: 0;
    right: 0;
    top: 400px;
    font-family: "Playfair Display", serif;
    font-weight: 700;
    font-size: 122px;
    line-height: 1;
    letter-spacing: 0.01em;
    color: var(--brand-blue);
  }
  .wine-estate {
    position: absolute;
    left: 0;
    right: 0;
    top: 578px;
    font-family: "Playfair Display", serif;
    font-weight: 400;
    font-size: 54px;
    line-height: 1;
    letter-spacing: 0.36em;
    padding-left: 0.36em;
    color: var(--ink);
  }
  .wine-type {
    position: absolute;
    left: 0;
    right: 0;
    top: 680px;
    font-family: "Montserrat", sans-serif;
    font-weight: 400;
    font-size: 52px;
    line-height: 1;
    letter-spacing: 0.04em;
    color: var(--ink);
  }
  .wine-abv {
    position: absolute;
    left: 0;
    right: 0;
    top: 844px;
    font-family: "Playfair Display", serif;
    font-style: italic;
    font-weight: 400;
    font-size: 29px;
    line-height: 1;
    color: var(--ink);
  }
</style>
</head>
<body>
  <main class="label">
    <div class="label__map" role="img" aria-label="Faint gold outline map of the vineyard region"></div>
    <div class="label__band label__band--top"></div>
    <div class="label__band label__band--bottom"></div>
    <div class="label__content">
      <div class="brand-mark"><span class="brand-mark__dot"></span><span>FERNHOLLOW</span></div>
      <h1 class="wine-name">FERNHOLLOW</h1>
      <p class="wine-estate">ESTATE</p>
      <p class="wine-type">RED WINE BLEND NV</p>
      <p class="wine-abv">Alc by Vol. 15.3%</p>
    </div>
  </main>
</body>
</html>
```